Business Card Design

Professional solutions in (servers, security, networks, programming)

Industry/Entity Type

Business

Contact Information for Business Card

Nadim Fouzan
Internet services and network solutions
TDK - GLPW - GLPT
netdesk@kavo-lin.com / 05291473806
www.kavo-lin.com

```html
<!DOCTYPE html>
<html lang="en">
<head>
<meta charset="utf-8">
<title>Nadim Fouzan – Business Card</title>
<link href="https://fonts.googleapis.com/css2?family=Exo+2:wght@300;400&display=swap" rel="stylesheet">
<style>
  :root {
    --backdrop: #d4d4d4;
    --card-dark: #414141;
    --accent-blue: #0a8fd6;
    --card-white: #ffffff;
    --text-white: #ffffff;
    --rule-grey: #cfcfcf;
  }
  html, body {
    margin: 0;
    padding: 0;
    width: 1200px;
    height: 1000px;
    overflow: hidden;
    background: var(--backdrop);
  }
  .canvas {
    position: relative;
    width: 1200px;
    height: 1000px;
    font-family: "Exo 2", "Trebuchet MS", sans-serif;
  }
  .card {
    position: absolute;
    left: 218px;
    top: 276px;
    width: 765px;
    height: 449px;
  }
  .card-shape {
    position: absolute;
    inset: 0;
  }
  .name {
    position: absolute;
    left: 44px;
    top: 48px;
    margin: 0;
    font-size: 64px;
    font-weight: 300;
    line-height: 1;
    letter-spacing: 1px;
    white-space: nowrap;
    color: var(--text-white);
  }
  .name .surname {
    color: var(--accent-blue);
    margin-left: 30px;
  }
  .name-rule {
    position: absolute;
    left: 44px;
    top: 138px;
    width: 531px;
    height: 1px;
    background: var(--text-white);
  }
  .services {
    position: absolute;
    right: 106px;
    top: 200px;
    text-align: right;
    font-size: 28px;
    line-height: 35px;
    font-weight: 400;
  }
  .services .tagline { color: var(--accent-blue); }
  .services .certs { color: var(--text-white); }
  .contact-rule {
    position: absolute;
    left: 243px;
    top: 330px;
    width: 415px;
    height: 1px;
    background: var(--rule-grey);
  }
  .contacts {
    position: absolute;
    left: 44px;
    top: 324px;
    margin: 0;
    padding: 0;
    list-style: none;
    font-size: 21px;
    line-height: 28px;
    color: var(--text-white);
  }
  .contacts .label {
    display: inline-block;
    width: 31px;
    color: var(--accent-blue);
  }
</style>
</head>
<body>
<div class="canvas">
  <div class="card">
    <svg class="card-shape" width="765" height="449" viewBox="0 0 765 449" aria-hidden="true">
      <defs>
        <clipPath id="card-outline">
          <rect x="0" y="0" width="765" height="449" rx="50" ry="50"/>
        </clipPath>
      </defs>
      <g clip-path="url(#card-outline)">
        <rect class="panel-dark" x="0" y="0" width="700" height="449" fill="var(--card-dark)"/>
        <rect class="stripe-blue" x="700" y="0" width="14" height="449" fill="var(--accent-blue)"/>
        <rect class="panel-white" x="714" y="0" width="51" height="449" fill="var(--card-white)"/>
      </g>
    </svg>

    <h1 class="name">NADIM<span class="surname">FOUZAN</span></h1>
    <div class="name-rule"></div>

    <div class="services">
      <div class="tagline">Internet services and network solutions</div>
      <div class="certs">TDK - GLPW - GLPT</div>
    </div>

    <div class="contact-rule"></div>
    <ul class="contacts">
      <li><span class="label">P:</span>05291473806</li>
      <li><span class="label">E:</span>netdesk@kavo-lin.com</li>
      <li><span class="label">W:</span>www.kavo-lin.com</li>
    </ul>
  </div>
</div>
</body>
</html>
```